Business Card - Professional Minimalist - Double sided

We appreciate minimalist logo/web/collateral designs that allow design to tell a story. We want to relay a professional image/approach but throwing in a splash of modern when we’re able so long as it’s not distracting. Think 75% classic corporate, 25% modern. Open to black or white design, not sure which might look the best.

Target Market(s)

Senior executives or related government affairs contacts within the agriculture, energy, and defense industries (i.e., potential clients) but located outside of Washington, DC. Most potential clients based in DC with be familiar with both of us and our shared history.

Industry/Entity Type

Consulting

Contact Information for Business Card

Name: Daniel R. Whitlock
Title: Co-Founder & Partner
Address: 418 Bramblewood Ave. SE | Suite 2716 | Washington, D.C. 20019
Phone: (202) 555-0187
Email: Daniel@HollerbyWhitlock.com

Font styles to use
Serif

Colors

Designer to choose only greyscale colors for use in the design.

Requirements
Must have
• Name: Daniel R. Whitlock
Phone: (202) 555-0187

```html
<!DOCTYPE html>
<html lang="en">
<head>
<meta charset="utf-8">
<title>Hollerby Whitlock Group – Business Card</title>
<link href="https://fonts.googleapis.com/css2?family=Marcellus&family=Tinos&display=swap" rel="stylesheet">
<style>
  :root {
    --backdrop: #c9cbca;
    --card: #332a29;
    --brand-muted: #5f5c5c;
    --name-grey: #5f5b5a;
    --title-grey: #a8a6a6;
    --rule-grey: #5a5453;
    --icon-grey: #5f5a59;
    --white: #ffffff;
  }
  * { margin: 0; padding: 0; box-sizing: border-box; }
  html, body { width: 1200px; height: 1200px; overflow: hidden; }
  body { background: var(--backdrop); position: relative; }

  .card {
    position: absolute;
    left: 222px;
    width: 762px;
    height: 436px;
    background: var(--card);
  }
  .card--front { top: 119px; }
  .card--back { top: 612px; }

  .brand { position: absolute; display: flex; align-items: flex-start; gap: 18px; }
  .card--front .brand { left: 111px; top: 96px; }
  .card--back .brand { left: 108px; top: 174px; }
  .brand__mark {
    width: 88px; height: 88px;
    border: 3px solid currentColor;
  }
  .brand__name {
    font-family: "Marcellus", serif;
    font-weight: 400;
    font-size: 36px;
    line-height: 1;
    letter-spacing: 1px;
    padding-top: 12px;
  }
  .brand__group {
    display: block;
    text-align: right;
    font-size: 22px;
    letter-spacing: 17px;
    margin-right: -17px;
    margin-top: 18px;
  }
  .card--front .brand { color: var(--brand-muted); }
  .card--back .brand { color: var(--white); }

  .person {
    position: absolute;
    right: 406px;
    top: 270px;
    text-align: right;
  }
  .person__name {
    font-family: "Tinos", serif;
    font-size: 33px;
    color: var(--name-grey);
    letter-spacing: 0.5px;
    line-height: 1;
  }
  .person__title {
    font-family: "Marcellus", serif;
    font-size: 21px;
    color: var(--title-grey);
    margin-top: 8px;
    margin-right: 4px;
    line-height: 1;
  }

  .divider {
    position: absolute;
    left: 374px; top: 243px;
    width: 2px; height: 146px;
    background: var(--rule-grey);
  }

  .contact { position: absolute; left: 394px; top: 252px; list-style: none; }
  .contact__item {
    display: flex; align-items: center; gap: 10px;
    height: 18px; margin-bottom: 11px;
    font-family: "Marcellus", serif;
    font-size: 12.5px;
    letter-spacing: 1.6px;
    color: var(--white);
    line-height: 1.15;
  }
  .contact__item--address { height: 28px; margin-bottom: 7px; }
  .contact__icon { width: 18px; height: 18px; flex: none; }
</style>
</head>
<body>

<section class="card card--front">
  <div class="brand">
    <span class="brand__mark"></span>
    <div class="brand__name">HOLLERBY WHITLOCK<span class="brand__group">GROUP</span></div>
  </div>

  <div class="person">
    <p class="person__name">Daniel R. Whitlock</p>
    <p class="person__title">Co-Founder &amp; Partner</p>
  </div>

  <span class="divider"></span>

  <ul class="contact">
    <li class="contact__item contact__item--address">
      <svg class="contact__icon" viewBox="0 0 18 18"><circle cx="9" cy="9" r="9" fill="var(--icon-grey)"/><path d="M9 4.2a3 3 0 0 0-3 3c0 2.3 3 6.3 3 6.3s3-4 3-6.3a3 3 0 0 0-3-3z" fill="var(--card)"/><circle cx="9" cy="7.2" r="1.1" fill="var(--icon-grey)"/></svg>
      <span>418 Bramblewood Ave. SE<br>| Suite 2716 | Washington, D.C. 20019</span>
    </li>
    <li class="contact__item">
      <svg class="contact__icon" viewBox="0 0 18 18"><circle cx="9" cy="9" r="9" fill="var(--icon-grey)"/><path d="M6 5.2l1.6-.4 1 2.2-1 .8a5 5 0 0 0 2.6 2.6l.8-1 2.2 1-.4 1.6c-3.5.3-7.1-3.3-6.8-6.8z" fill="var(--card)"/></svg>
      <span>(202) 555-0187</span>
    </li>
    <li class="contact__item">
      <svg class="contact__icon" viewBox="0 0 18 18"><circle cx="9" cy="9" r="9" fill="var(--icon-grey)"/><rect x="4.5" y="6" width="9" height="6.2" fill="none" stroke="var(--card)" stroke-width="1"/><path d="M4.5 6l4.5 3.6L13.5 6" fill="none" stroke="var(--card)" stroke-width="1"/></svg>
      <span>Daniel@HollerbyWhitlock.com</span>
    </li>
    <li class="contact__item">
      <svg class="contact__icon" viewBox="0 0 18 18"><circle cx="9" cy="9" r="9" fill="var(--icon-grey)"/><circle cx="9" cy="9" r="4.6" fill="none" stroke="var(--card)" stroke-width="1"/><path d="M4.4 9h9.2M9 4.4c-2 2.5-2 6.7 0 9.2M9 4.4c2 2.5 2 6.7 0 9.2" fill="none" stroke="var(--card)" stroke-width="0.8"/></svg>
      <span>www.hollerbywhitlock.com</span>
    </li>
  </ul>
</section>

<section class="card card--back">
  <div class="brand">
    <span class="brand__mark"></span>
    <div class="brand__name">HOLLERBY WHITLOCK<span class="brand__group">GROUP</span></div>
  </div>
</section>

</body>
</html>
```